Visual design for database driven web application

Need a clean, professional looking visual design for a web application.

PLUMB is the new standardized K-12 school testing program for the state of Texas. We are building an application named PLUMB-Finder (clever, yeah?) that will allow teachers, school administrators, and others to EASILY sort through millions of records of student data and print or export reports showing just the information they need about their students.

The state currently doesn't provide a user-friendly way to do this. They provide a "data dump" spreadsheet that school administrators and teachers must figure out how to manipulate to get the data they need. We are building a Web-based tool that will make it super simple and easy for our users to get the data they need in a format that works for them.

I've created a basic wireframe of the main application screen in Wirella Kit Plus. I need you to "skin" the wireframe to make it look good. Your mockup will set the tone for branding and visual design throughout the site.

See the attached screenshots. There are a few variations of the screen that include dynamic panels that open & close. Start by designing just the main screen and if you have time, do one or two of the panels. Thanks!
Updates

Target Market(s)

K-12 education professionals (teachers, administrators) in the state of Texas

Industry/Entity Type

Building

Requirements
Must have
• Your mockups should include all of the features & content shown in the attached screenshots.

However, you don't have to show all 10 rows of data. You can just do the column headers and one row of data. (It would be repetitive and unnecessary to spend time re-creating the entire grid with all of that data just to show your visual styling.)

The design should reflect the following concepts:

- Texas
- Education
- Simplicity
- Helpfulness
- Trust
- Professionalism

If I select your design, I will want your design source files (Illustrator, Photoshop, etc.)
Nice to have
• A logo in the upper left corner for PLUMB-Finder. The logo should definitely communicate the design concepts described under "must have."

```html
<!DOCTYPE html>
<html lang="en">
<head>
<meta charset="utf-8">
<title>PLUMB-Finder – Student Data</title>
<link href="https://fonts.googleapis.com/css2?family=Arimo:wght@400;700&display=swap" rel="stylesheet">
<style>
:root{
  --navy-top:#00108a;
  --navy-bottom:#1a2aa6;
  --brand-red:#c8102e;
  --text:#333333;
  --muted:#555555;
  --line:#cccccc;
  --row-alt:#f1f1f1;
  --white:#ffffff;
  --page-dark:#555555;
}
*{box-sizing:border-box;margin:0;padding:0}
html,body{width:1200px;height:751px;overflow:hidden;background:var(--white)}
body{font-family:"Arimo",Arial,sans-serif;color:var(--text)}
.stage{position:relative;width:1090px;height:682px;transform:scale(1.1009);transform-origin:0 0}
.abs{position:absolute}

/* header */
.app-header{position:absolute;left:0;top:0;width:1090px;height:101px;background:linear-gradient(var(--navy-top),var(--navy-bottom));border-bottom:4px solid var(--brand-red)}
.brand{left:40px;top:24px;display:flex;align-items:center;gap:10px;color:var(--white);font-size:26px;font-weight:700}
.brand-dot{width:20px;height:20px;border-radius:50%;background:var(--white)}
.user-nav{left:430px;top:40px;color:var(--white);font-size:13px;word-spacing:0}
.user-nav span{margin:0 18px 0 0}
.user-nav .sep{margin-right:20px}
.search{left:740px;top:34px;width:317px;height:30px;border:2px solid var(--brand-red);border-radius:4px;background:var(--white);overflow:hidden}
.search-btn{position:absolute;right:0;top:0;width:86px;height:100%;background:var(--brand-red);color:var(--white);font-size:15px;display:flex;align-items:center;justify-content:center}
.search-opts{left:874px;top:68px;color:var(--white);font-size:12.5px}
.search-opts u{margin-left:4px}
.tab{top:76px;font-size:14px;color:var(--white)}
.tab-plain{left:42px}
.tab-active{left:124px;top:72px;width:116px;height:25px;background:var(--brand-red);font-weight:700;display:flex;align-items:center;justify-content:center;border-radius:3px 3px 0 0}

/* panel */
.data-panel{left:16px;top:119px;width:1051px;height:457px;border:1px solid var(--line);border-radius:5px;background:linear-gradient(#f6f6f6,#ffffff 60px,#ffffff 400px,#f0f0f0)}
.summary{top:133px;font-size:14px;color:var(--muted)}
.summary-count{left:41px}
.summary-filter{left:431px}
.summary-filter u{color:var(--muted)}
.columns-tab{left:227px;top:125px;width:178px;height:33px;background:var(--white);border:1px solid var(--line);border-bottom:none;border-radius:4px 4px 0 0;font-size:14px;color:var(--muted);padding:7px 0 0 12px}
.rows-top{left:568px;top:176px;font-size:14px;color:var(--muted)}
.tool{top:180px;font-size:14px;color:var(--muted);display:flex;align-items:center;gap:5px}
.tool-print{left:898px}
.tool-download{left:969px}

/* grid */
.student-grid{position:absolute;left:16px;top:205px;width:1051px;border-collapse:collapse;table-layout:fixed;font-size:13px}
.student-grid th{background:var(--brand-red);color:var(--white);font-weight:400;height:28px;text-align:left;padding:0 7px}
.student-grid td{height:29.4px;padding:0 8px;border:1px solid #dddddd;border-top:none}
.student-grid tbody tr:nth-child(even) td{background:var(--row-alt)}

/* pager */
.pager{left:40px;top:539px;display:flex;gap:6px;align-items:center}
.page{width:24px;height:24px;border:1px solid #bbbbbb;border-radius:3px;background:linear-gradient(#ffffff,#e8e8e8);font-size:12px;display:flex;align-items:center;justify-content:center;color:var(--text)}
.page-wide{width:26px}
.page-current{background:var(--page-dark);color:var(--white);border-color:#444}
.page-gap{width:26px;text-align:center;font-size:12px}
.rows-control{left:436px;top:539px;display:flex;align-items:center;gap:5px;font-size:14px;color:var(--muted)}
.rows-select{width:46px;height:23px;border:1px solid #bbbbbb;border-radius:3px;background:var(--white);font-size:13px;padding:3px 0 0 5px;color:var(--text)}

/* column picker */
.column-picker{left:24px;top:157px;width:549px;height:298px;background:var(--white);border:1px solid var(--line);box-shadow:0 3px 8px rgba(0,0,0,.3)}
.picker-links{position:absolute;left:14px;top:11px;font-size:13px;color:var(--brand-red)}
.picker-links .sep{margin:0 10px}
.picker-rule{position:absolute;left:14px;width:507px;height:1px;background:var(--line)}
.option{position:absolute;font-size:13px;color:var(--muted);display:flex;align-items:center;gap:11px}
.box{width:13px;height:13px;border:1px solid #999;border-radius:2px;background:var(--white);position:relative}
.box.on::after{content:"";position:absolute;left:3px;top:0;width:4px;height:8px;border:solid #444;border-width:0 2px 2px 0;transform:rotate(45deg)}
.btn{position:absolute;top:254px;height:25px;border-radius:4px;background:var(--brand-red);color:var(--white);font-size:13.5px;display:flex;align-items:center;justify-content:center}
.btn-cancel{left:316px;width:78px}
.btn-apply{left:410px;width:78px}
</style>
</head>
<body>
<div class="stage">

  <header class="app-header">
    <div class="abs brand"><span class="brand-dot"></span>PLUMB-Finder</div>
    <div class="abs user-nav"><span>Welcome, Reed</span><span class="sep">|</span><span>My profile</span><span class="sep">|</span><span>Logout</span></div>
    <div class="abs search"><div class="search-btn">Search</div></div>
    <div class="abs search-opts">◂<u>search options</u></div>
    <div class="abs tab tab-plain">Instructions</div>
    <div class="abs tab tab-active">Student Data</div>
  </header>

  <section class="abs data-panel"></section>
  <div class="abs summary summary-count">Showing 26 of 38 columns</div>
  <div class="abs columns-tab">▼&nbsp; Show / Hide columns</div>
  <div class="abs summary summary-filter">3 columns are <u>filtered</u></div>
  <div class="abs rows-top">rows per page</div>
  <div class="abs tool tool-print">
    <svg width="20" height="17" viewBox="0 0 20 17"><rect x="5" y="0" width="10" height="5" fill="#555"/><rect x="0" y="5" width="20" height="8" rx="2" fill="#555"/><rect x="5" y="10" width="10" height="7" fill="#fff" stroke="#555" stroke-width="1.5"/></svg>Print
  </div>
  <div class="abs tool tool-download">
    <svg width="17" height="17" viewBox="0 0 17 17"><rect width="17" height="17" rx="2" fill="#555"/><path d="M4 4l4.5 4 4.5-4M4 9l4.5 4 4.5-4" stroke="#fff" stroke-width="2" fill="none"/></svg>Download
  </div>

  <table class="student-grid">
    <colgroup>
      <col style="width:51px"><col style="width:81px"><col style="width:63px"><col style="width:94px"><col style="width:86px"><col style="width:90px"><col style="width:122px"><col style="width:108px"><col style="width:52px"><col style="width:104px"><col style="width:75px"><col style="width:69px"><col style="width:56px">
    </colgroup>
    <thead>
      <tr><th>ESC</th><th>Grade</th><th>Year</th><th>District</th><th>Dist Name</th><th>Campus</th><th>Last Name</th><th>First Name</th><th>MI</th><th>Student ID</th><th>Genter</th><th>DOB</th><th>Hisp</th></tr>
    </thead>
    <tbody>
      <tr><td>411</td><td>9</td><td>10</td><td>999999001</td><td>Example</td><td>Example HS</td><td>Accountability</td><td>Marisol</td><td></td><td>630543340</td><td>F</td><td>7311996</td><td>1</td></tr>
      <tr><td>411</td><td>9</td><td>10</td><td>999999001</td><td>Example</td><td>Example HS</td><td>Accountability</td><td>Marisol</td><td></td><td>630543340</td><td>F</td><td>7311996</td><td>1</td></tr>
      <tr><td>411</td><td>9</td><td>10</td><td>999999001</td><td>Example</td><td>Example HS</td><td>Accountability</td><td>Marisol</td><td></td><td>630543340</td><td>F</td><td>7311996</td><td>1</td></tr>
      <tr><td>411</td><td>9</td><td>10</td><td>999999001</td><td>Example</td><td>Example HS</td><td>Accountability</td><td>Marisol</td><td></td><td>630543340</td><td>F</td><td>7311996</td><td>1</td></tr>
      <tr><td>411</td><td>9</td><td>10</td><td>999999001</td><td>Example</td><td>Example HS</td><td>Accountability</td><td>Marisol</td><td></td><td>630543340</td><td>F</td><td>7311996</td><td>1</td></tr>
      <tr><td>411</td><td>9</td><td>10</td><td>999999001</td><td>Example</td><td>Example HS</td><td>Accountability</td><td>Marisol</td><td></td><td>630543340</td><td>F</td><td>7311996</td><td>1</td></tr>
      <tr><td>411</td><td>9</td><td>10</td><td>999999001</td><td>Example</td><td>Example HS</td><td>Accountability</td><td>Marisol</td><td></td><td>630543340</td><td>F</td><td>7311996</td><td>1</td></tr>
      <tr><td>411</td><td>9</td><td>10</td><td>999999001</td><td>Example</td><td>Example HS</td><td>Accountability</td><td>Marisol</td><td></td><td>630543340</td><td>F</td><td>7311996</td><td>1</td></tr>
      <tr><td>411</td><td>9</td><td>10</td><td>999999001</td><td>Example</td><td>Example HS</td><td>Accountability</td><td>Marisol</td><td></td><td>630543340</td><td>F</td><td>7311996</td><td>1</td></tr>
      <tr><td>411</td><td>9</td><td>10</td><td>999999001</td><td>Example</td><td>Example HS</td><td>Accountability</td><td>Marisol</td><td></td><td>630543340</td><td>F</td><td>7311996</td><td>1</td></tr>
    </tbody>
  </table>

  <nav class="abs pager">
    <span class="page">‹</span><span class="page">1</span><span class="page">2</span><span class="page">3</span><span class="page page-current">4</span><span class="page">5</span><span class="page-gap">...</span><span class="page page-wide">10</span><span class="page page-wide">20</span><span class="page page-wide">30</span><span class="page">›</span>
  </nav>
  <div class="abs rows-control">Show <span class="rows-select">10 ⌄</span> rows&nbsp; per page</div>

  <div class="abs column-picker">
    <div class="picker-links">Check all<span class="sep">|</span>Uncheck all</div>
    <div class="picker-rule" style="top:34px"></div>

    <div class="option" style="left:24px;top:49px"><span class="box"></span>Date</div>
    <div class="option" style="left:24px;top:73px"><span class="box on"></span>Grade</div>
    <div class="option" style="left:24px;top:97px"><span class="box on"></span>ESC</div>
    <div class="option" style="left:24px;top:121px"><span class="box"></span>CDC</div>
    <div class="option" style="left:24px;top:145px"><span class="box on"></span>District</div>
    <div class="option" style="left:24px;top:169px"><span class="box on"></span>Capus</div>
    <div class="option" style="left:24px;top:193px"><span class="box on"></span>Last Name</div>
    <div class="option" style="left:24px;top:217px"><span class="box"></span>First Name</div>

    <div class="option" style="left:162px;top:49px"><span class="box"></span>MI</div>
    <div class="option" style="left:162px;top:73px"><span class="box on"></span>Student ID</div>
    <div class="option" style="left:162px;top:97px"><span class="box on"></span>Genter</div>
    <div class="option" style="left:162px;top:121px"><span class="box"></span>DOB</div>
    <div class="option" style="left:162px;top:145px"><span class="box on"></span>Hisp</div>
    <div class="option" style="left:162px;top:169px"><span class="box on"></span>AI/AN</div>
    <div class="option" style="left:162px;top:193px"><span class="box on"></span>Asian</div>
    <div class="option" style="left:162px;top:217px"><span class="box"></span>Af Am</div>

    <div class="option" style="left:293px;top:49px"><span class="box"></span>NH/PI</div>
    <div class="option" style="left:293px;top:73px"><span class="box on"></span>White</div>
    <div class="option" style="left:293px;top:97px"><span class="box on"></span>Eth</div>
    <div class="option" style="left:293px;top:121px"><span class="box"></span>ED</div>
    <div class="option" style="left:293px;top:145px"><span class="box on"></span>TI</div>
    <div class="option" style="left:293px;top:169px"><span class="box on"></span>Mig</div>
    <div class="option" style="left:293px;top:193px"><span class="box on"></span>LEP</div>
    <div class="option" style="left:293px;top:217px"><span class="box"></span>Bil</div>

    <div class="option" style="left:418px;top:49px"><span class="box"></span>MI</div>
    <div class="option" style="left:418px;top:73px"><span class="box on"></span>Student ID</div>
    <div class="option" style="left:418px;top:97px"><span class="box on"></span>Genter</div>
    <div class="option" style="left:418px;top:121px"><span class="box"></span>DOB</div>
    <div class="option" style="left:418px;top:145px"><span class="box on"></span>Hisp</div>
    <div class="option" style="left:418px;top:169px"><span class="box on"></span>AI/AN</div>
    <div class="option" style="left:418px;top:193px"><span class="box on"></span>Asian</div>
    <div class="option" style="left:418px;top:217px"><span class="box"></span>Af Am</div>

    <div class="picker-rule" style="top:245px"></div>
    <div class="btn btn-cancel">Cancel</div>
    <div class="btn btn-apply">Apply</div>
  </div>

</div>
</body>
</html>
```